Young, dynamic furniture company needs a new business card design

We require a new business card design for our modern furniture company which supplies furniture and appliances to the property and development market.
Oakline Furnishings has become one of the leading furniture & appliance suppliers to the property market withing London. With over 10 years experience, we have increased our business to supply not only private landlords and managing agents, but also property developers, housing associations and local councils.
We offer not only a complete range of furniture which includes beds, wardrobes, dining sets and sofas, but also a high quality, full delivery and assembly service to help you with all our furnishing needs.

Target Market(s)

Private landlords, estate agents, letting agents, property management companies

Industry/Entity Type

Business

Contact Information for Business Card

Name,
Title,
Address,
Mobile,
Telephone,
Fax, Website, email address

Font styles to use
Sans Serif

Colors
3176b5
0555a3
85abd2
cfdeed

Requirements
Must have
• All the above information for each of our staff, along with our logo

```html
<!DOCTYPE html>
<html lang="en">
<head>
<meta charset="utf-8">
<title>Oakline Furnishings – Business Card</title>
<link href="https://fonts.googleapis.com/css2?family=Roboto:wght@400;700;900&display=swap" rel="stylesheet">
<style>
  :root {
    --bg: #e9ecf0;
    --card: #ffffff;
    --ink: #2b2b2d;
    --blue-deep: #0555a3;
    --blue: #3176b5;
    --blue-soft: #85abd2;
    --blue-pale: #cfdeed;
    --white: #ffffff;
  }
  * { margin: 0; padding: 0; box-sizing: border-box; }
  html, body { width: 1200px; height: 923px; overflow: hidden; }
  body {
    background: var(--bg);
    font-family: "Roboto", Arial, sans-serif;
    position: relative;
  }
  .card {
    position: absolute;
    left: 250px;
    width: 700px;
    height: 400px;
    background: var(--card);
    border-radius: 20px;
    overflow: hidden;
    box-shadow: 0 6px 20px rgba(0,0,0,.15);
  }
  .card--back { top: 40px; }
  .card--front { top: 483px; }

  .brand { position: absolute; display: flex; flex-direction: column; color: var(--ink); }
  .brand__row { display: flex; align-items: center; gap: 14px; }
  .brand__mark { width: 26px; height: 26px; background: var(--blue); }
  .brand__name { font-weight: 400; text-transform: uppercase; letter-spacing: 1px; }
  .brand__tag { text-transform: uppercase; color: var(--ink); letter-spacing: .5px; }

  .card--back .brand { left: 0; right: 0; top: 130px; align-items: center; }
  .card--back .brand__name { font-size: 34px; }
  .card--back .brand__tag { font-size: 14px; margin-top: 6px; }
  .card--back .site {
    position: absolute; left: 0; right: 0; top: 270px;
    text-align: center; font-size: 18px; font-weight: 700; color: var(--ink);
  }

  .card--front .brand { left: 40px; top: 50px; }
  .card--front .brand__name { font-size: 27px; }
  .card--front .brand__tag { font-size: 12px; margin-top: 4px; margin-left: 40px; }

  .band { position: absolute; inset: 0; width: 100%; height: 100%; }
  .band__fill { fill: var(--blue-deep); }

  .person { position: absolute; right: 40px; top: 168px; text-align: right; }
  .person__name { font-size: 22px; font-weight: 900; color: var(--blue-deep); }
  .person__title { font-size: 17px; color: var(--ink); margin-top: 2px; }

  .address {
    position: absolute; left: 36px; top: 262px;
    color: var(--white); font-size: 18px; line-height: 1.35;
  }
  .contacts {
    position: absolute; right: 36px; top: 294px;
    list-style: none; color: var(--white); font-size: 16px; line-height: 20px;
  }
  .contacts li { display: flex; justify-content: flex-end; align-items: center; gap: 10px; }
  .contacts svg { width: 15px; height: 15px; fill: var(--white); flex: none; }
  .contacts .icon-line { fill: none; stroke: var(--white); stroke-width: 1.4; }
</style>
</head>
<body>

<section class="card card--back" aria-label="Card back">
  <div class="brand">
    <div class="brand__row">
      <span class="brand__mark"></span>
      <span class="brand__name">Oakline Furnishings</span>
    </div>
    <span class="brand__tag">Trade Furniture Solutions</span>
  </div>
  <p class="site">www.oaklinefurnishings.com</p>
</section>

<section class="card card--front" aria-label="Card front">
  <svg class="band" viewBox="0 0 700 400" preserveAspectRatio="none" aria-hidden="true">
    <path class="band__fill" d="M0,215 C200,250 450,240 700,285 L700,400 L0,400 Z"/>
  </svg>

  <div class="brand">
    <div class="brand__row">
      <span class="brand__mark"></span>
      <span class="brand__name">Oakline Furnishings</span>
    </div>
    <span class="brand__tag">Trade Furniture Solutions</span>
  </div>

  <div class="person">
    <p class="person__name">Daniel Reeve</p>
    <p class="person__title">Job Title</p>
  </div>

  <p class="address">34 Street Name<br>City Name, Country 4567</p>

  <ul class="contacts">
    <li>000 1234 5678
      <svg viewBox="0 0 16 16"><path d="M3 1h3l1 4-2 1c1 2 3 4 5 5l1-2 4 1v3c0 1-1 2-2 2C7 15 1 9 1 3c0-1 1-2 2-2z"/></svg></li>
    <li>000 1234 5678
      <svg viewBox="0 0 16 16"><path d="M4 0h8a1 1 0 0 1 1 1v14a1 1 0 0 1-1 1H4a1 1 0 0 1-1-1V1a1 1 0 0 1 1-1zm1 2v10h6V2zm3 11a1 1 0 1 0 0 2 1 1 0 0 0 0-2z"/></svg></li>
    <li>000 1234 5678
      <svg viewBox="0 0 16 16"><path d="M4 0h8v4H4zM1 5h14v7h-3v4H4v-4H1zm4 5v5h6v-5z"/></svg></li>
    <li>info@oaklinefurnishings.com
      <svg viewBox="0 0 16 16"><path d="M0 3h16v10H0zm1.5 1L8 9l6.5-5z"/></svg></li>
    <li>www.oaklinefurnishings.com
      <svg viewBox="0 0 16 16"><g class="icon-line"><circle cx="8" cy="8" r="6.8"/><ellipse cx="8" cy="8" rx="3" ry="6.8"/><path d="M1.2 8h13.6M2.2 4.5h11.6M2.2 11.5h11.6"/></g></svg></li>
  </ul>
</section>

</body>
</html>
```